New business card with our logo

we finalized our logo with the help of pixel harbor - now we need a business card using that logo. we are a metal service center providing raw steel and metal products for fabricating, contractors, artists, etc. we have the wording for the back of the card figured out (attached, no deviations from text please), just need help putting it all together.
would like the look of steel somehow incorporated in the design ... would like the black part of the logo to be steel or silver color (the S & BRANLEY)
Other font styles liked:
- calibri, arial, similar to those, modern looking
Colors
Designer to choose colors to be used in the design.
Requirements
Must have
- Back of card must haves are attached (no deviations from wording please).
- FRONT of card:
- logo
- address
- name
- office tel
- cell
- fax
- website
- address
Nice to have
- incorporate the look of steel or element of steel somehow
- names of the staff on front not in all caps, i.e. Rosvita not ROSVITA
- this industry is more industrial, not coffee or flower shop so design should be aligned with that
- design should be classic and tasteful

```html
<!DOCTYPE html>
<html lang="en">
<head>
<meta charset="utf-8">
<title>Branley Steel – Business Card</title>
<link href="https://fonts.googleapis.com/css2?family=Roboto:ital,wght@0,400;0,500;0,700;1,500&display=swap" rel="stylesheet">
<style>
  :root{
    --canvas:#e6e7e9;
    --card-dark:#2a2a2c;
    --card-dark-edge:#232325;
    --paper:#ffffff;
    --ink:#111113;
    --steel:#c8cacc;
    --steel-light:#eceef0;
    --steel-dark:#8d9093;
    --blue:#1a73c2;
    --muted:#d6d7d9;
  }
  *{box-sizing:border-box;margin:0;padding:0}
  html,body{width:806px;height:1200px;overflow:hidden}
  body{background:var(--canvas);font-family:"Roboto",Arial,sans-serif;position:relative}

  .card{position:absolute;left:83px;width:640px;height:365px;overflow:hidden;
        box-shadow:0 6px 18px rgba(0,0,0,.18)}
  .card--front{top:200px;background:var(--paper)}
  .card--back{top:635px;background:radial-gradient(ellipse at 50% 40%,#333336 0%,var(--card-dark) 55%,var(--card-dark-edge) 100%)}

  /* front */
  .brand-panel{position:absolute;left:0;top:0;width:314px;height:365px;
        background:radial-gradient(ellipse at 50% 45%,#333336 0%,var(--card-dark) 60%,var(--card-dark-edge) 100%);
        display:flex;flex-direction:column;align-items:center;justify-content:center;gap:18px}
  .brand-mark{width:96px;height:96px;border-radius:50%;border:7px solid var(--blue)}
  .brand-name{color:var(--steel);font-weight:700;font-size:50px;line-height:1;text-align:center;letter-spacing:.5px}
  .steel-strip{position:absolute;left:304px;top:26px;width:9px;height:313px;
        background:linear-gradient(90deg,var(--steel-dark),var(--steel-light) 50%,var(--steel))}
  .edge-bar{position:absolute;left:607px;top:41px;width:33px;height:288px;background:var(--card-dark)}
  .edge-line{position:absolute;left:602px;top:41px;width:2px;height:288px;background:var(--card-dark)}

  .holder-name{position:absolute;left:337px;top:48px;font-size:29px;font-weight:500;color:var(--ink);letter-spacing:.2px}
  .contact-list{list-style:none}
  .contact{position:absolute;right:49px;display:flex;align-items:center;gap:12px;
        font-size:14px;color:var(--ink);text-align:right;line-height:1.15}
  .contact__icon{width:42px;height:42px;border-radius:50%;background:var(--card-dark);
        display:flex;align-items:center;justify-content:center;flex:none}
  .contact__icon svg{width:24px;height:24px}

  /* back */
  .back-head{position:absolute;top:46px;left:0;width:100%;display:flex;justify-content:center;align-items:center;gap:20px}
  .back-head .brand-mark{width:86px;height:86px;border-width:6px}
  .back-head .brand-name{font-size:40px;white-space:nowrap}
  .service-title{position:absolute;top:146px;width:100%;text-align:center;color:var(--muted);font-size:31px;font-weight:500;letter-spacing:.3px}
  .service-list{position:absolute;top:187px;width:100%;text-align:center;color:var(--muted);font-size:17px;letter-spacing:.4px;word-spacing:2px}
  .rule{position:absolute;top:220px;left:122px;width:412px;height:2px;background:var(--muted)}
  .products{position:absolute;top:239px;width:100%;text-align:center;color:var(--muted);font-size:17px;font-weight:500;line-height:1.35}
  .tagline{position:absolute;top:297px;width:100%;text-align:center;color:var(--steel-light);font-size:20px;font-style:italic;font-weight:500}
</style>
</head>
<body>

<section class="card card--front" aria-label="Card front">
  <div class="brand-panel">
    <div class="brand-mark"></div>
    <div class="brand-name">BRANLEY<br>STEEL</div>
  </div>
  <div class="steel-strip"></div>
  <div class="edge-line"></div>
  <div class="edge-bar"></div>

  <h1 class="holder-name">CUSTOMER NAME</h1>
  <ul class="contact-list">
    <li class="contact" style="top:92px">+01 123 456 789
      <span class="contact__icon"><svg viewBox="0 0 24 24" fill="none" stroke="#fff" stroke-width="1.8"><rect x="7" y="2.5" width="10" height="19" rx="2"/><line x1="11" y1="18.5" x2="13" y2="18.5"/></svg></span></li>
    <li class="contact" style="top:139px">+01 1234 567 78
      <span class="contact__icon"><svg viewBox="0 0 24 24" fill="none" stroke="#fff" stroke-width="1.8"><rect x="7" y="3" width="10" height="5"/><rect x="3.5" y="8" width="17" height="8" rx="1.5"/><rect x="7" y="13" width="10" height="7" fill="#2a2a2c"/></svg></span></li>
    <li class="contact" style="top:186px">lorem@ipsum.com
      <span class="contact__icon"><svg viewBox="0 0 24 24" fill="none" stroke="#fff" stroke-width="1.8"><rect x="3.5" y="6" width="17" height="12" rx="1"/><polyline points="3.5,6 12,13 20.5,6"/></svg></span></li>
    <li class="contact" style="top:231px">loremwebsite.com
      <span class="contact__icon"><svg viewBox="0 0 24 24" fill="none" stroke="#fff" stroke-width="1.5"><circle cx="12" cy="12" r="8.5"/><ellipse cx="12" cy="12" rx="3.8" ry="8.5"/><line x1="3.5" y1="12" x2="20.5" y2="12"/><path d="M5 7.5h14M5 16.5h14"/></svg></span></li>
    <li class="contact" style="top:280px">Street Adress Name, 0123<br>Cityname, 012345
      <span class="contact__icon"><svg viewBox="0 0 24 24" fill="#fff"><path d="M12 2.5a6.5 6.5 0 0 0-6.5 6.5c0 5 6.5 12.5 6.5 12.5s6.5-7.5 6.5-12.5A6.5 6.5 0 0 0 12 2.5zm0 9.3a2.8 2.8 0 1 1 0-5.6 2.8 2.8 0 0 1 0 5.6z"/></svg></span></li>
  </ul>
</section>

<section class="card card--back" aria-label="Card back">
  <div class="back-head">
    <div class="brand-mark"></div>
    <div class="brand-name">BRANLEY STEEL</div>
  </div>
  <h2 class="service-title">METAL SERVICE CENTER</h2>
  <p class="service-list">CUT &nbsp;•&nbsp; SHEAR &nbsp;•&nbsp; PUNCH &nbsp;•&nbsp; LIGHT FAB</p>
  <div class="rule"></div>
  <p class="products">Structural Steel &nbsp;•&nbsp; Stainless &amp; Aluminum<br>Building Components &nbsp;•&nbsp; Rebar &nbsp;•&nbsp; Decking ...and more!</p>
  <p class="tagline">Cut to size, Pick-up or Delivered!</p>
</section>

</body>
</html>
```